Personal creative Biz Card Design

Need personal yet natural and organic design. The cards I have now are well designed but look too commercial. I want more organic FEELING kind of card. I thought having a headshot would make it more personal... but maybe a sketch effect (or line drawing effect) of face better (?). Maybe in a gray or tungsten color?

Target Market(s)

Well, everyone i give card to will have already seen me face-to-face so that is one thing. Mostly yoga students and people interested in improving their fitness or general health. People looking for wellness, a personal fitness trainer, a yoga teacher

Industry/Entity Type

Health And Wellness

Contact Information for Business Card

I provided examples

Requirements
Must have
• My main logo
• My name

```html
<!DOCTYPE html>
<html lang="en">
<head>
<meta charset="utf-8">
<title>Noel Avery – Business Card</title>
<link href="https://fonts.googleapis.com/css2?family=Open+Sans:wght@400;600&display=swap" rel="stylesheet">
<style>
  :root {
    --backdrop: #1c1c1c;
    --card: #ffffff;
    --green: #4a9a2e;
    --green-dark: #2f7a22;
    --green-light: #6cbf45;
    --ink: #333333;
    --muted: #666666;
    --frame: #111111;
    --badge-blue: #2a3f8f;
    --badge-red: #d8242f;
    --badge-navy: #1f3566;
  }
  * { box-sizing: border-box; margin: 0; padding: 0; }
  html, body { width: 1200px; height: 900px; overflow: hidden; }
  body {
    background: var(--backdrop);
    font-family: "Open Sans", Arial, sans-serif;
    position: relative;
  }
  .card {
    position: absolute;
    top: 170px;
    width: 347px;
    height: 561px;
    background: var(--card);
  }
  .card--front { left: 259px; }
  .card--back { left: 631px; }

  .accent-bar {
    position: absolute;
    left: 94px;
    width: 159px;
    height: 29px;
    background: linear-gradient(180deg, var(--green-light), var(--green-dark));
  }
  .accent-bar--top { top: 0; }
  .accent-bar--bottom { bottom: 0; background: linear-gradient(0deg, var(--green-light), var(--green-dark)); }

  .portrait {
    position: absolute;
    left: 91px;
    top: 57px;
    width: 159px;
    height: 235px;
    border: 3px solid var(--frame);
    background: linear-gradient(180deg, #f4f2ec 0%, #e6e1d4 55%, #cfc9b8 100%);
  }

  .contact {
    position: absolute;
    top: 313px;
    left: 0;
    width: 100%;
    list-style: none;
    text-align: center;
    color: var(--ink);
    font-size: 16.5px;
    line-height: 27.5px;
  }
  .contact li { display: flex; justify-content: center; align-items: center; gap: 9px; }
  .contact svg { width: 12px; height: 12px; fill: var(--green); flex: none; }

  .badge { position: absolute; }
  .badge--circle {
    left: 6px; top: 409px; width: 64px; height: 64px;
    border-radius: 50%; border: 4px solid var(--frame); background: #fff;
  }
  .badge--bar-a { left: 100px; top: 422px; width: 106px; height: 34px; }
  .badge--bar-b { left: 229px; top: 414px; width: 112px; height: 42px; }
  .badge--bar-c { left: 57px; top: 484px; width: 103px; height: 36px; }
  .badge--studio {
    left: 178px; top: 486px; display: flex; align-items: center; gap: 5px;
    color: var(--green); font-size: 10px; font-weight: 600; width: 100px; line-height: 12px;
  }
  .badge--studio .dot { width: 14px; height: 14px; border-radius: 50%; background: var(--green); flex: none; }

  .brand {
    position: absolute;
    left: 42px;
    top: 135px;
    width: 290px;
  }
  .brand-name {
    display: flex; align-items: center; gap: 10px;
    color: var(--green); font-size: 28px; font-weight: 600; letter-spacing: 0.5px;
  }
  .brand-name .dot { width: 20px; height: 20px; border-radius: 50%; background: var(--green); }
  .brand-tagline {
    margin-top: 4px; padding-left: 30px;
    color: var(--muted); font-size: 12.5px;
  }

  .services {
    position: absolute;
    top: 290px;
    left: 0;
    width: 100%;
    list-style: none;
    text-align: center;
    color: var(--green);
    font-size: 17px;
    line-height: 22.8px;
  }
</style>
</head>
<body>
  <section class="card card--front">
    <div class="accent-bar accent-bar--top"></div>
    <div class="portrait" role="img" aria-label="Portrait photo of the yoga teacher in a light sweater"></div>
    <ul class="contact">
      <li><svg viewBox="0 0 24 24"><path d="M6.6 10.8a15.1 15.1 0 0 0 6.6 6.6l2.2-2.2c.3-.3.7-.4 1-.2 1.1.4 2.3.6 3.6.6.6 0 1 .4 1 1V20c0 .6-.4 1-1 1A17 17 0 0 1 3 4c0-.6.4-1 1-1h3.5c.6 0 1 .4 1 1 0 1.3.2 2.5.6 3.6.1.3 0 .7-.2 1z"/></svg>555-014-2287</li>
      <li><svg viewBox="0 0 24 24"><path d="M2 5h20v14H2z M3 6l9 7 9-7" stroke="#fff" stroke-width="1.5"/></svg>noelinnerpaths@example.com</li>
      <li><svg viewBox="0 0 24 24"><circle cx="12" cy="12" r="10"/></svg>www.noelavery.com</li>
    </ul>
    <div class="badge badge--circle" role="img" aria-label="Registered teacher certificate badge"></div>
    <svg class="badge badge--bar-a" viewBox="0 0 106 34" role="img" aria-label="Exercise council certification badge"><rect x="0" y="4" width="106" height="24" fill="var(--badge-blue)"/><rect x="0" y="30" width="106" height="3" fill="var(--badge-red)"/></svg>
    <svg class="badge badge--bar-b" viewBox="0 0 112 42" role="img" aria-label="Certified trainer badge"><rect x="0" y="6" width="60" height="28" fill="var(--badge-blue)"/><rect x="60" y="14" width="52" height="5" fill="var(--badge-red)"/></svg>
    <svg class="badge badge--bar-c" viewBox="0 0 103 36" role="img" aria-label="Sports medicine academy badge"><rect x="0" y="6" width="103" height="24" fill="var(--badge-navy)"/></svg>
    <div class="badge badge--studio"><span class="dot"></span>Noel Avery Studio</div>
    <div class="accent-bar accent-bar--bottom"></div>
  </section>

  <section class="card card--back">
    <div class="brand">
      <div class="brand-name"><span class="dot"></span>NOEL AVERY</div>
      <p class="brand-tagline">Expert Guidance for a Healthier Life</p>
    </div>
    <ul class="services">
      <li>Teacher of Yogo</li>
      <li>Leader of Yogo Teacher Trainings</li>
      <li>Personal Fitness Trainer</li>
      <li>Private &amp; Public classes/Sessions</li>
      <li>Nutrition, Wellness, Meditation</li>
      <li>Healing ceremonies (Puja &amp; Shamanic)</li>
      <li>Certified &amp; Insured</li>
    </ul>
  </section>
</body>
</html>
```